Refresh our business cards

Our client is an online store and requires a business card refresh

The guideline and visual identity of this brand;
1. Typography - bold
2. Key Colours - Blue and white with a touch of black as per the logo
3. Brand Elements - minimalistic and simple

Visual Identity
1. Logo - we have attached the current logo but open to suggested improvements
2. Business Cards: will include
logo, company address, email, name, facebook handle, instagram handle, twitter handle, website.

note all material, once accepted, needs to be in usable format.

WE REQUIRE A VERY GOOD RESULTS THAT CONSIDERS ALL THE ITEMS WE REQUIRE.
The business card needs to be editable so we can add other employee names to the card as required.

File format required are: ai, esp, jpg, png, pdf,

```html
<!DOCTYPE html>
<html lang="en">
<head>
<meta charset="utf-8">
<title>Bright Gem Studio – Business Cards</title>
<link rel="stylesheet" href="https://fonts.googleapis.com/css2?family=Lato:wght@300;400;700&display=swap">
<style>
  :root {
    --backdrop: #8b8e93;
    --card: #ffffff;
    --ink: #1b1b1b;
    --ink-soft: #4a4a4a;
    --brand-blue: #2a8fd1;
    --icon-bg: #1b1b1b;
    --icon-fg: #ffffff;
  }
  * { box-sizing: border-box; margin: 0; padding: 0; }
  html, body { width: 1200px; height: 900px; overflow: hidden; }
  body {
    background: var(--backdrop);
    font-family: "Lato", sans-serif;
    color: var(--ink);
    position: relative;
  }
  .card {
    position: absolute;
    width: 525px;
    height: 300px;
    background: var(--card);
    border-radius: 22px;
  }
  .card--contact { left: 50px; top: 300px; }
  .card--brand { left: 625px; top: 300px; }

  /* brand lockup */
  .brand {
    display: flex;
    align-items: center;
    gap: 12px;
  }
  .brand__circle {
    width: 46px; height: 46px;
    border: 2px solid var(--brand-blue);
    border-radius: 50%;
    flex: none;
  }
  .brand__name {
    font-weight: 300;
    font-size: 19px;
    letter-spacing: 1.5px;
    text-transform: uppercase;
    color: var(--ink-soft);
    line-height: 1.15;
  }
  .brand__url {
    font-size: 12px;
    color: var(--brand-blue);
    margin-top: 10px;
  }

  /* brand side */
  .card--brand .brand-block {
    position: absolute;
    left: 150px;
    top: 95px;
  }
  .card--brand .brand__circle { width: 70px; height: 70px; }
  .card--brand .brand__name { font-size: 22px; }
  .card--brand .brand__url { font-size: 14px; }

  /* contact side */
  .person {
    position: absolute;
    left: 32px;
    top: 26px;
  }
  .person__name { font-size: 26px; font-weight: 400; }
  .person__title { font-size: 11px; color: var(--ink-soft); margin-top: 2px; }
  .rule {
    position: absolute;
    left: 0; right: 0;
    height: 2px;
    background: var(--brand-blue);
  }
  .rule--one { top: 82px; }
  .rule--two { top: 88px; }

  .contacts {
    list-style: none;
    position: absolute;
    display: flex;
    flex-direction: column;
    gap: 6px;
  }
  .contacts--primary { left: 32px; top: 108px; }
  .contacts--secondary { left: 250px; top: 205px; gap: 7px; }
  .contacts li {
    display: flex;
    align-items: center;
    gap: 8px;
    font-size: 12px;
  }
  .contacts--secondary li { font-size: 14px; }
  .icon {
    width: 18px; height: 18px;
    flex: none;
    display: block;
  }
  .card--contact .brand-block {
    position: absolute;
    left: 300px;
    top: 110px;
  }
  .card--contact .brand__circle { width: 38px; height: 38px; }
  .card--contact .brand__name { font-size: 14px; }
  .card--contact .brand__url { font-size: 9px; margin-top: 6px; }
</style>
</head>
<body>

<section class="card card--contact" aria-label="Business card, contact side">
  <div class="person">
    <h1 class="person__name">Elena Varossi</h1>
    <p class="person__title">Creative Managing Director</p>
  </div>
  <div class="rule rule--one"></div>
  <div class="rule rule--two"></div>

  <ul class="contacts contacts--primary">
    <li>
      <svg class="icon" viewBox="0 0 18 18" aria-hidden="true"><circle cx="9" cy="9" r="9" fill="var(--icon-bg)"/><path d="M6 4.5h2l.8 2.3-1.2.9a6 6 0 0 0 2.7 2.7l.9-1.2 2.3.8v2c0 .6-.5 1-1 1A7.5 7.5 0 0 1 5 5.5c0-.5.4-1 1-1z" fill="var(--icon-fg)"/></svg>
      <span>+61 3 9555 0142</span>
    </li>
    <li>
      <svg class="icon" viewBox="0 0 18 18" aria-hidden="true"><circle cx="9" cy="9" r="9" fill="var(--icon-bg)"/><rect x="6.3" y="4" width="5.4" height="10" rx="1" fill="var(--icon-fg)"/><rect x="7.1" y="5.2" width="3.8" height="6.5" fill="var(--icon-bg)"/></svg>
      <span>+61 4 9155 0187</span>
    </li>
    <li>
      <svg class="icon" viewBox="0 0 18 18" aria-hidden="true"><circle cx="9" cy="9" r="9" fill="var(--icon-bg)"/></svg>
      <span>@brightgem</span>
    </li>
    <li>
      <svg class="icon" viewBox="0 0 18 18" aria-hidden="true"><circle cx="9" cy="9" r="9" fill="var(--icon-bg)"/><rect x="4.5" y="5.5" width="9" height="7" fill="var(--icon-fg)"/><path d="M4.5 5.5 9 9.3l4.5-3.8" fill="none" stroke="var(--icon-bg)" stroke-width="1"/></svg>
      <span>elena@brightgemstudio.com.au</span>
    </li>
    <li>
      <svg class="icon" viewBox="0 0 18 18" aria-hidden="true"><circle cx="9" cy="9" r="9" fill="var(--icon-bg)"/></svg>
      <span>bright_gem_studio</span>
    </li>
  </ul>

  <div class="brand-block">
    <div class="brand">
      <span class="brand__circle"></span>
      <span class="brand__name">Bright Gem<br>Studio</span>
    </div>
    <p class="brand__url">www.brightgemstudio.com.au</p>
  </div>

  <ul class="contacts contacts--secondary">
    <li>
      <svg class="icon" viewBox="0 0 18 18" aria-hidden="true"><circle cx="9" cy="9" r="9" fill="var(--icon-bg)"/></svg>
      <span>brightgemstudio</span>
    </li>
    <li>
      <svg class="icon" viewBox="0 0 18 18" aria-hidden="true"><circle cx="9" cy="9" r="9" fill="var(--icon-bg)"/><g fill="none" stroke="var(--icon-fg)" stroke-width="1"><circle cx="9" cy="9" r="4.8"/><ellipse cx="9" cy="9" rx="2" ry="4.8"/><path d="M4.2 9h9.6"/></g></svg>
      <span>www.brightgemstudio.com.au</span>
    </li>
    <li>
      <svg class="icon" viewBox="0 0 18 18" aria-hidden="true"><circle cx="9" cy="9" r="9" fill="var(--icon-bg)"/><path d="M9 3.8a3.6 3.6 0 0 0-3.6 3.6c0 2.7 3.6 6.6 3.6 6.6s3.6-3.9 3.6-6.6A3.6 3.6 0 0 0 9 3.8z" fill="var(--icon-fg)"/><circle cx="9" cy="7.4" r="1.3" fill="var(--icon-bg)"/></svg>
      <span>14/220 Harbour Lane Fairview</span>
    </li>
  </ul>
</section>

<section class="card card--brand" aria-label="Business card, brand side">
  <div class="brand-block">
    <div class="brand">
      <span class="brand__circle"></span>
      <span class="brand__name">Bright Gem<br>Studio</span>
    </div>
    <p class="brand__url">www.brightgemstudio.com.au</p>
  </div>
</section>

</body>
</html>
```